Fresh Start Bold Body Challenge 2017 Poster

We are having a Fresh Start, Bold Body Challenge for 2017 at our fitness studio. We need a poster design using the template attached as a reference (Only reference). I have also included our Vorbelix logo to put on the poster. Please DO NOT use the graphics in the flyer as we are expecting something much much better :-)
MUST HAVES:
- Size needed 11x17 with bleeding for printing
- .PSD File Format WITH LAYERS (CS3 Compatible)*** A MUST
- Use Vorbelix Bootcamps Logo
- Use Information in the attached word doc

```html
<!DOCTYPE html>
<html lang="en">
<head>
<meta charset="utf-8">
<title>Vorbelix Bootcamps – Fresh Start, Bold Body Challenge 2017</title>
<link rel="stylesheet" href="https://fonts.googleapis.com/css2?family=Black+Ops+One&family=Montserrat:wght@400;600;700;800&family=Oswald:wght@500;700&display=swap">
<style>
  :root {
    --ink: #0b0b0d;
    --white: #f4f4f4;
    --tan: #c9a05a;
    --gold: #e0a94a;
    --blue: #2f6fc0;
    --blue-deep: #1d4f97;
    --red: #d9201f;
    --orange: #e58a1f;
    --grey: #8d8f94;
    --copper: #b0562d;
  }
  * { box-sizing: border-box; margin: 0; padding: 0; }
  html, body { width: 775px; height: 1200px; overflow: hidden; background: var(--ink); }
  .poster {
    position: relative;
    width: 775px;
    height: 1200px;
    overflow: hidden;
    background:
      radial-gradient(ellipse at 70% 35%, #2a2c31 0%, transparent 55%),
      linear-gradient(160deg, #1b1c20 0%, var(--ink) 60%);
    font-family: "Montserrat", sans-serif;
    color: var(--white);
  }
  .photo { position: absolute; }
  .photo--athlete-woman {
    right: 0; top: 0; width: 400px; height: 440px;
    background: linear-gradient(200deg, #5a3a2c 0%, #7a4b33 35%, #b8342e 55%, #2a1e1c 80%, transparent 100%);
    clip-path: polygon(18% 0, 100% 0, 100% 100%, 0 70%);
    opacity: .9;
  }
  .photo--athlete-man {
    left: 0; top: 500px; width: 470px; height: 490px;
    background: radial-gradient(ellipse at 35% 45%, #c98a62 0%, #9b6142 40%, #4a2d22 75%, transparent 100%);
  }
  .photo--dumbbell {
    left: 300px; top: 720px; width: 170px; height: 150px;
    background: radial-gradient(circle at 55% 50%, #4a4b4f 0%, #222327 60%, transparent 72%);
  }
  .logo {
    position: absolute; left: 50px; top: 62px;
    width: 245px; height: 66px;
    background: var(--white);
    border: 3px solid var(--grey);
    display: flex; align-items: center; gap: 10px; padding: 0 14px;
  }
  .logo__mark { width: 16px; height: 16px; background: var(--blue-deep); flex: none; }
  .logo__name { font-weight: 800; font-size: 21px; color: var(--blue-deep); letter-spacing: .5px; line-height: 1.15; }
  .headline {
    position: absolute; display: flex; justify-content: center; align-items: center;
    white-space: nowrap; font-family: "Black Ops One", sans-serif; line-height: 1;
  }
  .headline--top { top: 214px; left: 40px; width: 600px; font-size: 64px; color: var(--blue); }
  .headline--main { top: 292px; left: 20px; width: 640px; font-size: 86px; color: var(--tan); gap: 14px; }
  .headline--sub { top: 398px; left: 40px; width: 600px; font-size: 60px; color: var(--white); letter-spacing: 1px; }
  .stopwatch {
    flex: none; width: 48px; height: 70px;
    background: radial-gradient(circle at 50% 55%, #e8e8e8 0%, #9ea0a4 55%, #d6b23a 70%, transparent 72%);
    opacity: .85;
  }
  .tab {
    position: absolute; left: 300px; top: 497px; height: 34px; width: 250px;
    background: var(--blue); color: var(--white);
    font-weight: 700; font-size: 20px; line-height: 34px; text-align: center;
  }
  .tab__rule { position: absolute; left: 550px; top: 505px; width: 225px; height: 7px; background: var(--orange); }
  .pitch { position: absolute; left: 300px; top: 545px; font-weight: 800; line-height: 1; }
  .pitch__big { font-size: 48px; color: var(--red); }
  .pitch__small { font-size: 34px; color: var(--blue); margin-top: 10px; padding-left: 36px; }
  .promise { position: absolute; left: 572px; top: 552px; font-size: 22px; line-height: 1.3; color: var(--gold); }
  .schedule { position: absolute; right: 32px; top: 668px; text-align: right; color: var(--gold); }
  .schedule__title { font-weight: 600; font-size: 27px; line-height: 1.1; }
  .schedule__date { font-size: 17px; line-height: 1.25; }
  .schedule__label { font-size: 17px; margin-top: 16px; line-height: 1.25; }
  .finale { position: absolute; right: 32px; top: 840px; font-weight: 600; font-size: 27px; color: var(--gold); }
  .finale b { color: var(--blue); font-weight: 600; }
  .stripe {
    position: absolute; left: 262px; top: 918px; width: 540px; height: 44px;
    background: var(--white); transform: rotate(-3deg); transform-origin: left bottom;
    color: var(--red); font-weight: 800; font-size: 21px; line-height: 44px; padding-left: 28px;
    white-space: nowrap;
  }
  .cash-band {
    position: absolute; left: 0; top: 962px; width: 775px; height: 78px;
    background: linear-gradient(180deg, var(--blue) 0%, var(--blue-deep) 100%);
    display: flex; align-items: center; padding-left: 34px; gap: 16px;
    font-family: "Oswald", sans-serif;
  }
  .cash-band__amount { font-size: 56px; font-weight: 700; }
  .cash-band__divider { width: 4px; height: 44px; background: var(--white); }
  .cash-band__note { font-size: 36px; font-weight: 500; }
  .badge { position: absolute; left: 40px; top: 800px; width: 250px; height: 190px; }
  .badge__text { position: absolute; left: 45px; top: 840px; width: 240px; text-align: center; transform: rotate(-8deg); }
  .badge__lead { font-weight: 700; font-size: 24px; }
  .badge__price { font-weight: 800; font-size: 66px; color: var(--red); line-height: 1; }
  .contact { position: absolute; left: 0; top: 1108px; width: 775px; text-align: center; font-size: 24px; color: var(--copper); }
  .contact__site { color: var(--blue); font-weight: 700; font-size: 30px; margin-left: 8px; }
</style>
</head>
<body>
<main class="poster">
  <div class="photo photo--athlete-woman" role="img" aria-label="Photo of a female athlete in a red sports top doing a push-up"></div>
  <div class="photo photo--athlete-man" role="img" aria-label="Photo of a muscular male athlete lifting a dumbbell"></div>
  <div class="photo photo--dumbbell" role="img" aria-label="Photo of a dumbbell"></div>

  <div class="logo"><span class="logo__mark"></span><span class="logo__name">Vorbelix Bootcamps</span></div>

  <h1>
    <span class="headline headline--top">FRESH START</span>
    <span class="headline headline--main">BOLD<span class="stopwatch" role="img" aria-label="Illustration of a stopwatch with a measuring tape"></span>BODY</span>
    <span class="headline headline--sub">CHALLENGE</span>
  </h1>

  <div class="tab">6 Weeks Contest</div>
  <div class="tab__rule"></div>

  <div class="pitch">
    <div class="pitch__big">Transform</div>
    <div class="pitch__small">YOUR BODY</div>
  </div>
  <p class="promise">Get In The<br>Best Shape<br>Of Your Life!</p>

  <div class="schedule">
    <div class="schedule__title">Kick Off Meeting</div>
    <div class="schedule__date">Thursday, Jan 12th&nbsp; at 7:30 pm</div>
    <div class="schedule__label">Start Date<br>Tuesday, January 17th</div>
    <div class="schedule__date">End Date<br>Saturday, February 25th</div>
  </div>
  <div class="finale">Finale Party <b>March 2nd</b></div>

  <div class="stripe">6 Weeks : Training, Nutrition, Coaching</div>

  <div class="cash-band">
    <span class="cash-band__amount">$500 CASH</span>
    <span class="cash-band__divider"></span>
    <span class="cash-band__note">Prize for Winner!</span>
  </div>

  <svg class="badge" viewBox="0 0 250 190" aria-hidden="true">
    <polygon points="20,40 150,4 235,80 190,186 40,180" fill="#0b0b0d" stroke="#f4f4f4" stroke-width="7"/>
  </svg>
  <div class="badge__text">
    <div class="badge__lead">Starting at</div>
    <div class="badge__price">$99!</div>
  </div>

  <p class="contact">Visit for more info :<span class="contact__site">vorbelixbootcamps.com</span></p>
</main>
</body>
</html>
```